We need a web page design for a new company called "Quarry". We provide an innovative music sharing mobile application that allows music listeners to share their music without paying for a monthly subscription. We would like to incorporate the attached logo and color scheme. The final design should communicate music gifting and sharing.

Industry/Entity Type

It Company

```html
<!DOCTYPE html>
<html lang="en">
<head>
<meta charset="utf-8">
<title>Quarry – share the music</title>
<link rel="stylesheet" href="https://fonts.googleapis.com/css2?family=Arimo:wght@400;700&family=Noto+Serif:ital,wght@0,700;1,400&family=Ubuntu:wght@500&display=swap">
<style>
  :root {
    --green: #5ea805;
    --green-text: #4f9a00;
    --black: #000;
    --white: #fff;
    --ink: #111;
    --grey-head: #777;
    --grey-text: #6b6b6b;
    --grey-light: #aaa;
    --rule: #d6d6d6;
    --device: #1a1a1a;
  }
  * { box-sizing: border-box; margin: 0; padding: 0; }
  html, body { width: 1200px; height: 1000px; overflow: hidden; background: var(--white); }
  body { position: relative; font-family: "Arimo", Arial, sans-serif; }
  .abs { position: absolute; }

  .hero-band { left: 0; top: 0; width: 1200px; height: 423px; background: var(--green); }
  .hero-device {
    left: 265px; top: 66px; width: 200px; height: 389px; border-radius: 34px;
    background: linear-gradient(160deg, #3a3a3a 0%, var(--device) 45%, #000 100%);
    border: 2px solid #bbb;
  }
  .hero-device .screen {
    position: absolute; left: 15px; top: 66px; width: 166px; height: 252px;
    background: linear-gradient(180deg, var(--green) 0 22%, #f2f2f2 22% 55%, var(--green) 55% 70%, #f2f2f2 70%);
  }
  .brand { left: 537px; top: 70px; display: flex; align-items: center; gap: 12px; }
  .brand .mark { width: 48px; height: 48px; border-radius: 50%; background: var(--white); }
  .brand .name { font-family: "Ubuntu", sans-serif; font-weight: 500; font-size: 54px; color: var(--white); line-height: 1; }
  .hero-copy { left: 548px; top: 175px; width: 380px; color: var(--white); font-size: 13.5px; line-height: 21px; }
  .hero-links { left: 552px; top: 279px; font-size: 11px; color: var(--white); }
  .hero-links b { color: var(--ink); }
  .hero-links a { color: var(--ink); font-style: italic; }
  .store-badge { left: 552px; top: 322px; width: 151px; height: 53px; border-radius: 6px; background: var(--black); border: 2px solid var(--white); }

  .quote { left: 265px; top: 489px; width: 295px; font-family: "Noto Serif", serif; font-style: italic; font-size: 12px; line-height: 17px; color: #555; }
  .quote-by { left: 265px; top: 559px; font-family: "Noto Serif", serif; font-style: italic; font-size: 10.5px; color: var(--grey-text); }
  .quote-by b { font-style: normal; color: var(--green-text); }
  .trust-title { left: 657px; top: 470px; font-size: 18px; font-weight: 700; color: var(--grey-head); }
  .trust-copy { left: 660px; top: 508px; width: 290px; font-size: 10px; line-height: 17px; color: var(--grey-text); }
  .trust-links { left: 660px; top: 590px; font-size: 9.5px; color: var(--grey-text); }
  .trust-links b { color: var(--green-text); }
  .trust-links a { color: var(--green-text); font-style: italic; }

  .divider { left: 0; top: 631px; width: 1200px; height: 1px; background: var(--rule); }
  .features-title { left: 264px; top: 655px; font-size: 18px; font-weight: 700; color: #8a8a8a; }
  .feature h3 { position: absolute; top: 729px; font-size: 10.5px; color: var(--green-text); }
  .feature p { position: absolute; top: 754px; width: 222px; font-size: 9.5px; line-height: 14px; color: var(--grey-text); }
  .feature-device {
    top: 726px; width: 92px; height: 110px; border-radius: 12px; background: var(--black);
  }
  .feature-device .screen { position: absolute; left: 6px; top: 31px; width: 80px; height: 80px; background: var(--green); }

  .footer { left: 0; top: 825px; width: 1200px; height: 175px; background: var(--black); text-align: center; }
  .footer-links { position: absolute; top: 58px; width: 100%; font-size: 8.5px; color: var(--grey-light); }
  .footer-copy { position: absolute; top: 77px; width: 100%; font-size: 10.5px; color: #bbb; }
  .social { position: absolute; top: 101px; left: 568px; display: flex; gap: 12px; }
  .social span { width: 24px; height: 24px; border-radius: 50%; background: var(--white); }
  .social span:first-child { background: var(--green); }
</style>
</head>
<body>
  <div class="abs hero-band"></div>
  <div class="abs hero-device" role="img" aria-label="Smartphone showing the Quarry app playlist screen">
    <div class="screen"></div>
  </div>

  <div class="abs brand">
    <span class="mark"></span>
    <span class="name">Quarry</span>
  </div>
  <p class="abs hero-copy">Lorem Ipsum is simply dummy text of the printing and typesetting industry. Lorem Ipsum has been the industry's standard dummy text</p>
  <p class="abs hero-links"><b>LEARN MORE</b> or <a>view screenshots</a></p>
  <div class="abs store-badge" role="img" aria-label="App store download badge"></div>

  <p class="abs quote">“ Lorem Ipsum is simply dummy text of the printing and typesetting industry. Lorem Ipsum has been the industry's standard dummy text ever since. ”</p>
  <p class="abs quote-by">- <b>Lorem Ipsum Simple</b> Name</p>

  <h2 class="abs trust-title">THE ONES YOU CAN TRUST</h2>
  <p class="abs trust-copy">Lorem Ipsum is simply dummy text of the printing and typesetting industry. Lorem Ipsum has been the industry's standard dummy text ever since the 1500s, when an unknown printer took a galley of type and scrambled</p>
  <p class="abs trust-links"><b>READ MORE ABOUT US</b> or <a>see our work</a></p>

  <div class="abs divider"></div>
  <h2 class="abs features-title">See App Features..</h2>

  <div class="feature">
    <h3 style="left:264px">Cool Feature 1</h3>
    <p style="left:264px">Lorem Ipsum is simply dummy text of the printing and typesetting industry. Lorem Ipsum has been the industry's standard dummy text ever since the 1500s, when</p>
    <div class="abs feature-device" style="left:499px" role="img" aria-label="Phone showing the Quarry app"><div class="screen"></div></div>
  </div>
  <div class="feature">
    <h3 style="left:635px">Cool Feature 2</h3>
    <p style="left:635px">Lorem Ipsum is simply dummy text of the printing and typesetting industry. Lorem Ipsum has been the industry's standard dummy text ever since the 1500s, when</p>
    <div class="abs feature-device" style="left:870px" role="img" aria-label="Phone showing the Quarry app"><div class="screen"></div></div>
  </div>

  <footer class="abs footer">
    <p class="footer-links">Site Link | Privacy Policy | Terms &amp; Condition</p>
    <p class="footer-copy">Copyright © 2014 Company Name.</p>
    <div class="social" aria-label="Social links"><span></span><span></span><span></span></div>
  </footer>
</body>
</html>
```